Business Card Design

We are a new motor lodge in Hamilton NZ. Providing luxury accommodation and excellent service is the core of our business. We are looking for a different business card to capture the eye once in there hand. We have quite a lot of different clientele, corporate, travellers passing by plus we are positioned by two main hospitals so we have a lot of guests staying from there.
The existing card we have has a bed in the background with our logo. Does not stand out too much.

Maisie

To our final designers we will be making a decision today. we will be intouch

Target Market(s)

Quite a variety from single travellers to families

Industry/Entity Type

Accommodation

Contact Information for Business Card

Pelora Motor Lodge Maisie & Gareth Lund
18 Wirimu Crescent Hamilton 3204
Freephone 0800 519 364
Phone 07 946 3381
Fax 07 9463382
info@peloramotorlodge-example.co.nz
www.peloramotorlodge-example.co.nz

Colors

Designer to choose colors to be used in the design.

Requirements
Must have
• Name:
Address:
Phone Numbers:
Web and Email Addresses.
Pelora Logo
map on the back of our positioning
Nice to have
• Something styley and eyecatching have included a couple of photos of the Motor Lodge

```html
<!DOCTYPE html>
<html lang="en">
<head>
<meta charset="utf-8">
<title>Pelora Motor Lodge – Business Card</title>
<link rel="stylesheet" href="https://fonts.googleapis.com/css2?family=Open+Sans:wght@300;400;700&display=swap">
<style>
  :root {
    --page-bg: #e9e6e1;
    --card-black: #0b0b0d;
    --card-charcoal: #2a2b30;
    --band-blue: #3e5a8c;
    --band-navy: #1d2a4a;
    --ice-blue: #8fc3e8;
    --text-white: #f2f4f7;
    --logo-plate: #1a1b1f;
    --sky-blue: #4a78b8;
    --dusk-blue: #7f9fc9;
    --street-amber: #c9763c;
    --street-rust: #8a4a2c;
  }
  * { box-sizing: border-box; margin: 0; padding: 0; }
  html, body {
    width: 1200px; height: 646px; overflow: hidden;
    background: var(--page-bg);
    font-family: "Open Sans", Arial, sans-serif;
  }
  .canvas {
    position: relative; width: 1200px; height: 646px;
    display: flex; align-items: center; justify-content: center; gap: 60px;
  }
  .card {
    position: relative; width: 510px; height: 300px; overflow: hidden;
    box-shadow: 0 6px 18px rgba(0,0,0,.25);
  }

  /* Contact side */
  .card--contact {
    background: radial-gradient(ellipse at 55% 25%, var(--card-charcoal) 0%, var(--card-black) 60%);
    color: var(--text-white);
  }
  .contact__band {
    position: absolute; left: 0; top: 0; width: 100%; height: 62px;
    background: linear-gradient(90deg, var(--band-navy) 0%, var(--band-blue) 45%, var(--band-navy) 100%);
    border-bottom: 1px solid rgba(255,255,255,.35);
  }
  .contact__address {
    position: absolute; right: 18px; top: 14px;
    font-size: 12px; font-weight: 700; letter-spacing: 1.4px;
    text-transform: uppercase; color: var(--text-white);
  }
  .contact__brand {
    position: absolute; left: 26px; top: 78px;
    display: flex; align-items: center; gap: 10px;
  }
  .brand-mark {
    width: 14px; height: 14px; background: var(--ice-blue);
  }
  .brand-name {
    font-size: 24px; font-weight: 700; color: var(--ice-blue);
    text-transform: uppercase; letter-spacing: 1px; line-height: 1;
  }
  .contact__people {
    position: absolute; right: 26px; top: 126px;
    font-size: 19px; font-weight: 300; color: var(--ice-blue);
  }
  .contact__web {
    position: absolute; right: 26px; top: 160px; text-align: right;
    font-size: 10px; line-height: 15px; color: var(--text-white);
  }
  .contact__phones {
    position: absolute; left: 26px; bottom: 22px;
    font-size: 13px; line-height: 18px; color: var(--text-white);
  }
  .contact__phones span { color: var(--ice-blue); }

  /* Photo side */
  .card--photo { background: var(--sky-blue); }
  .photo__scene {
    position: absolute; inset: 0;
    background: linear-gradient(180deg, var(--sky-blue) 0%, var(--dusk-blue) 38%, var(--street-amber) 72%, var(--street-rust) 100%);
  }
  .photo__brand {
    position: absolute; left: 22px; top: 52px;
    padding: 16px 20px; background: var(--logo-plate);
    display: flex; align-items: center; gap: 10px;
  }
</style>
</head>
<body>
<main class="canvas">
  <section class="card card--contact" aria-label="Business card contact side">
    <div class="contact__band"></div>
    <p class="contact__address">18 Wirimu Crescent Hamilton 3204</p>
    <div class="contact__brand">
      <span class="brand-mark"></span>
      <span class="brand-name">Pelora Motor Lodge</span>
    </div>
    <p class="contact__people">Maisie &amp; Gareth Lund</p>
    <p class="contact__web">info@peloramotorlodge-example.co.nz<br>www.peloramotorlodge-example.co.nz</p>
    <p class="contact__phones">
      Freephone <span>0800 519 364</span><br>
      Phone <span>07 946 3381</span><br>
      Fax <span>07 9463382</span>
    </p>
  </section>

  <section class="card card--photo" aria-label="Business card photo side">
    <div class="photo__scene" role="img" aria-label="Photograph of the motor lodge buildings at dusk with light trails on the street"></div>
    <div class="photo__brand">
      <span class="brand-mark"></span>
      <span class="brand-name">Pelora Motor Lodge</span>
    </div>
  </section>
</main>
</body>
</html>
```